Design Powerpoint template for US based family office

Corvale Stewardship Group is the investment firm of a family based in the US. All of our investments have a financial return but also a social or environmental good. We care about the impact our money has on society and manage our firm to reflect those beliefs. We are in need of a powerpoint template for presentations that we give at conferences. This should incorporate our logo and be easy to print. Slides will vary and include text, charts, graphics and maps. Formatted options for each should be included in the template.

Target Market(s)

Other investors and startup entrepreneurs looking for funding. Our website is here in case it helps get a sense of our work: http://corvalestewardshipgroup.example/

Industry/Entity Type

Finance

Font styles to use
Sans Serif

Colors
0255a3
85cae6

Requirements
Must have
• Look very professional, clean lines etc. Built in graphics templates in the same color scheme are also important. Our logo should also be included on each slide in some way, page numbers are also important on all slides except the first title slide.

```html
<!DOCTYPE html>
<html lang="en">
<head>
<meta charset="utf-8">
<title>Corvale Stewardship Group – Slide Template</title>
<link href="https://fonts.googleapis.com/css2?family=Open+Sans:wght@400;600;700&display=swap" rel="stylesheet">
<style>
  :root {
    --brand-blue: #0255a3;
    --brand-sky: #85cae6;
    --brand-mid: #3b86c8;
    --brand-deep: #013f7a;
    --ink: #222;
    --muted: #666;
    --stage: #8e8e8e;
    --paper: #fff;
    --rule: #d5d5d5;
  }
  * { box-sizing: border-box; margin: 0; padding: 0; }
  html, body { width: 849px; height: 1200px; overflow: hidden; }
  body { background: var(--stage); font-family: "Open Sans", Arial, sans-serif; color: var(--ink); position: relative; }

  .slide { position: absolute; left: 40px; width: 770px; height: 557px; background: var(--paper); overflow: hidden; }
  .slide--chart { top: 22px; }
  .slide--contact { top: 607px; }

  .site-url { position: absolute; top: 12px; right: 24px; font-size: 10px; font-weight: 600; color: var(--brand-blue); }
  .slide-title { position: absolute; left: 40px; top: 44px; font-size: 30px; line-height: 34px; font-weight: 700; color: var(--ink); text-transform: uppercase; }
  .slide-title .accent { color: var(--brand-blue); }
  .slide-subtitle { position: absolute; left: 40px; top: 124px; font-size: 17px; color: var(--ink); }

  .pie { position: absolute; left: 40px; top: 160px; width: 340px; height: 250px; }
  .legend { position: absolute; left: 70px; top: 418px; display: flex; gap: 12px; font-size: 9px; color: var(--muted); }
  .legend span::before { content: ""; display: inline-block; width: 7px; height: 7px; margin-right: 3px; background: var(--swatch); }

  .categories { position: absolute; left: 470px; top: 150px; width: 230px; list-style: none; }
  .categories li { margin-bottom: 18px; }
  .categories h3 { font-size: 12px; font-weight: 400; color: var(--ink); margin-bottom: 3px; }
  .categories p { font-size: 8px; line-height: 11px; color: var(--muted); }

  .footer { position: absolute; left: 0; bottom: 12px; width: 100%; height: 66px; background: var(--brand-blue); color: var(--paper); }
  .footer-strip { position: absolute; left: 0; bottom: 0; width: 100%; height: 12px; background: var(--brand-sky); }
  .brand-name { position: absolute; left: 24px; top: 18px; font-size: 17px; line-height: 18px; font-weight: 600; letter-spacing: 1px; text-transform: uppercase; }
  .brand-name small { display: block; font-size: 9px; letter-spacing: 2px; }
  .pager { position: absolute; left: 398px; top: 24px; display: flex; align-items: center; gap: 10px; font-size: 11px; }
  .pager-btn { width: 16px; height: 16px; background: var(--brand-mid); display: flex; align-items: center; justify-content: center; }
  .contact { position: absolute; left: 580px; top: 8px; font-size: 10px; line-height: 14px; }
  .contact h4 { font-size: 12px; font-weight: 400; color: var(--brand-sky); margin-bottom: 2px; }

  .body-copy { position: absolute; left: 40px; top: 186px; width: 300px; font-size: 11px; line-height: 17px; color: var(--muted); }
  .social { position: absolute; left: 40px; list-style: none; font-size: 11px; color: var(--ink); }
  .social li { display: flex; align-items: center; gap: 14px; margin-bottom: 26px; }
  .social .mark { width: 24px; height: 24px; background: var(--brand-deep); }
  .divider { position: absolute; left: 385px; top: 60px; width: 1px; height: 400px; background: var(--rule); }
  .map { position: absolute; left: 415px; top: 58px; width: 320px; height: 172px; background: var(--brand-blue); color: var(--paper); display: flex; align-items: center; justify-content: center; font-size: 17px; }
  .details { position: absolute; left: 415px; top: 260px; font-size: 9px; line-height: 12px; color: var(--muted); }
  .details dt { color: var(--ink); }
  .details dd { margin-bottom: 16px; }
  .details .link { color: var(--brand-blue); }
</style>
</head>
<body>

<section class="slide slide--chart">
  <div class="site-url">www.corvalestewardshipgroup.example</div>
  <h1 class="slide-title">Sample of<br>Graph <span class="accent">Chart</span></h1>
  <p class="slide-subtitle">Some title in this line</p>

  <svg class="pie" viewBox="-170 -130 340 250" role="img" aria-label="Pie chart of four categories">
    <g transform="translate(0,22) scale(1,0.6)">
      <circle r="150" fill="#013f7a"/>
    </g>
    <g transform="scale(1,0.6)">
      <path d="M0,0 L0,-150 A150,150 0 0 1 75,129.9 Z" fill="#0255a3"/>
      <path d="M0,0 L75,129.9 A150,150 0 0 1 -114.9,96.4 Z" fill="#85cae6"/>
      <path d="M0,0 L-114.9,96.4 A150,150 0 0 1 -129.9,-75 Z" fill="#5fb0dc"/>
      <path d="M0,0 L-129.9,-75 A150,150 0 0 1 0,-150 Z" fill="#1f6fb8"/>
    </g>
  </svg>
  <div class="legend">
    <span style="--swatch:#0255a3">Category 1</span>
    <span style="--swatch:#85cae6">Category 2</span>
    <span style="--swatch:#5fb0dc">Category 3</span>
    <span style="--swatch:#1f6fb8">Category 4</span>
  </div>

  <ul class="categories">
    <li><h3>Category 1</h3><p>Lorem Ipsum is simply dummy text of the printing and typesetting industry. Lorem Ipsum is simply.</p></li>
    <li><h3>Category 2</h3><p>Lorem Ipsum is simply dummy text of the printing and typesetting industry. Lorem Ipsum is simply.</p></li>
    <li><h3>Category 3</h3><p>Lorem Ipsum is simply dummy text of the printing and typesetting industry. Lorem Ipsum is simply.</p></li>
    <li><h3>Category 4</h3><p>Lorem Ipsum is simply dummy text of the printing and typesetting industry. Lorem Ipsum is simply.</p></li>
  </ul>

  <footer class="footer">
    <div class="brand-name">Corvale<small>Stewardship Group</small></div>
    <div class="pager"><span class="pager-btn">&#9664;</span>5 &nbsp;OF&nbsp; 8<span class="pager-btn">&#9654;</span></div>
    <div class="contact"><h4>Contact Us</h4>482 Alder Row (rear unit)<br>Marrow Bend, NM 87999</div>
  </footer>
  <div class="footer-strip"></div>
</section>

<section class="slide slide--contact">
  <div class="site-url">www.corvalestewardshipgroup.example</div>
  <h1 class="slide-title">Sample of<br>Graph <span class="accent">Chart</span></h1>
  <p class="slide-subtitle">Some title in this line</p>

  <p class="body-copy">All of our investments have a financial return but also a social or environmental good. We care about the impact our money has on society and manage our firm to reflect those beliefs. We are in need of a powerpoint template for presentations that we give at conferences.</p>

  <ul class="social" style="top:372px">
    <li><span class="mark"></span>social-one.example/your-add</li>
    <li><span class="mark"></span>social-two.example/your-add</li>
  </ul>

  <div class="divider"></div>
  <div class="map" role="img" aria-label="Map showing the office location">Map here</div>

  <dl class="details">
    <dt>Address:</dt>
    <dd>Lorem Ipsum dolor, 50063<br>Lorem, Country</dd>
    <dt>Phone:</dt>
    <dd>+ 1 123 123 123456</dd>
    <dt>Email Id:</dt>
    <dd class="link">www.corvalestewardshipgroup.example</dd>
  </dl>

  <footer class="footer">
    <div class="brand-name">Corvale<small>Stewardship Group</small></div>
    <div class="pager"><span class="pager-btn">&#9664;</span>6 &nbsp;OF&nbsp; 8<span class="pager-btn">&#9654;</span></div>
    <div class="contact"><h4>Contact Us</h4>482 Alder Row (rear unit)<br>Marrow Bend, NM 87999</div>
  </footer>
  <div class="footer-strip"></div>
</section>

</body>
</html>
```